Broschüre für Toben – Tollen – Balancieren
Zielgruppe
Wir bieten Rangel und Raufkurse für Kinder ab dem Vorschulalter bis zu weiterführenden Schulen. Die Broschüre erhalten Lehrer, Erzieher und Direktoren der Einrichtungen an denen die Kurse Angeboten werden.
Aufgabenstellung
Design sollte eher Schlicht und modern wirken und an der homepage
www.boden-lernwerk.de orientiert sein.
Infobroschüre zum Durchblättern, kein Folder. Seitenfolge wie auf der Powerpoint präsentation.

```html
<!DOCTYPE html>
<html lang="de">
<head>
<meta charset="utf-8">
<title>Toben – Tollen – Balancieren · Broschüre Seite 8–9</title>
<link href="https://fonts.googleapis.com/css2?family=Open+Sans:ital,wght@0,400;0,600;0,700;0,800;1,400;1,700&display=swap" rel="stylesheet">
<style>
  :root {
    --backdrop: #dcdcdc;
    --paper: #ffffff;
    --brand-red: #9c1a1a;
    --box-red: #9a1515;
    --ink: #4a4a4a;
    --ink-soft: #6d6d6d;
    --ink-dark: #333333;
    --rule-grey: #9a9a9a;
  }
  * { margin: 0; padding: 0; box-sizing: border-box; }
  html, body {
    width: 1200px; height: 833px; overflow: hidden;
    background: var(--backdrop);
    font-family: "Open Sans", Arial, sans-serif;
    color: var(--ink);
  }
  .spread {
    position: absolute; left: 48px; top: 26px;
    width: 1104px; height: 780px;
    display: flex;
  }
  .page {
    position: relative; width: 552px; height: 780px;
    background: var(--paper); overflow: hidden;
  }
  .page--left { box-shadow: inset -14px 0 18px -14px rgba(0,0,0,.18); }
  .page--right { box-shadow: inset 14px 0 18px -14px rgba(0,0,0,.18); }

  .headline {
    position: absolute; color: var(--brand-red);
    font-weight: 600; font-size: 25px; letter-spacing: .3px; white-space: nowrap;
  }
  .headline-rule {
    position: absolute; width: 34px; height: 2px; background: var(--brand-red);
  }

  /* left page */
  .page--left .headline { left: 42px; top: 58px; }
  .page--left .headline-rule { left: 42px; top: 104px; }
  .intro {
    position: absolute; left: 42px; top: 122px; width: 470px;
    font-weight: 700; font-size: 11px; line-height: 15px; color: var(--ink-dark);
  }
  .intro .drop-cap {
    float: left; font-size: 46px; line-height: 40px; font-weight: 800;
    margin: 2px 6px 0 0; color: var(--ink-dark);
  }
  .col { position: absolute; font-size: 8.4px; line-height: 13px; color: var(--ink-soft); }
  .col p + p { margin-top: 12px; }
  .col--l1 { left: 42px; top: 200px; width: 212px; }
  .col--l2 { left: 280px; top: 200px; width: 232px; }
  .units { list-style: none; margin-top: 10px; }
  .units li { margin-bottom: 11px; }
  .units strong { display: block; color: var(--ink-dark); font-weight: 700; }

  .photo { position: absolute; }
  .photo--kids {
    left: 0; top: 452px; width: 552px; height: 240px;
    background: linear-gradient(100deg, #b9bcc0 0%, #8da3a6 30%, #b56b6d 48%, #4f5e7a 62%, #c9cfd2 100%);
  }

  .page-number {
    position: absolute; bottom: 26px; font-size: 8.5px;
    letter-spacing: .6px; color: var(--ink-soft);
  }
  .page-number::before {
    content: ""; position: absolute; top: -6px; width: 1px; height: 34px; background: var(--rule-grey);
  }
  .page--left .page-number { left: 40px; padding-left: 8px; }
  .page--left .page-number::before { left: 0; }
  .page--right .page-number { right: 40px; padding-right: 8px; }
  .page--right .page-number::before { right: 0; }

  .brand-name {
    position: absolute; bottom: 30px;
    font-size: 9px; font-weight: 700; letter-spacing: 1px; color: var(--ink-soft);
  }
  .page--left .brand-name { right: 40px; bottom: 62px; }
  .page--right .brand-name { left: 40px; }

  /* right page */
  .photo--mats {
    left: 0; top: 0; width: 552px; height: 290px;
    background: linear-gradient(160deg, #ecebe8 0%, #dcd9d4 40%, #d8403d 62%, #e0584f 80%, #f1eeea 100%);
  }
  .page--right .headline { left: 40px; top: 318px; }
  .page--right .headline-rule { left: 40px; top: 362px; }
  .col--r1 { left: 40px; top: 380px; width: 225px; }
  .col--r2 { left: 290px; top: 380px; width: 222px; }
  .col strong { color: var(--ink-dark); font-weight: 700; }

  .quote-box {
    position: absolute; top: 530px; width: 228px; height: 168px;
    background: var(--box-red); border-radius: 8px; color: #fff;
    padding: 14px 14px; font-size: 8.2px; line-height: 12.6px;
  }
  .quote-box--a { left: 40px; }
  .quote-box--b { left: 284px; }
  .quote-label { font-weight: 700; font-size: 8.6px; margin-bottom: 6px; }
  .quote-author { font-weight: 700; display: flex; gap: 5px; align-items: flex-start; }
  .quote-author svg { flex: none; margin-top: 2px; }
  .quote-text { margin-top: 2px; }
  .quote-text--italic { font-style: italic; }
</style>
</head>
<body>
<main class="spread">
  <section class="page page--left">
    <h1 class="headline">Sichere Kinder – Sicherer Start</h1>
    <div class="headline-rule"></div>
    <p class="intro"><span class="drop-cap">W</span>ir stärken Kinder auf ihrem Weg ins Schulleben. Selbstsicherheit und souveränes Auftreten sind die wichtigsten Bausteine, nicht nur für einen gelingenden Schulstart, sondern auch für eine erfolgreiche Zukunft.</p>

    <div class="col col--l1">
      <p>Dabei ist es wichtig, Kinder auf Gefahren aufmerksam zu machen – ohne sie dabei zu verängstigen. Im Umgang mit Kindern im Vor- und Grundschulalter ist es besonders wichtig, die Inhalte spielerisch und unbeschwert zu vermitteln. Die verbalen und körperlichen Abwehrstrategien werden durch Rollenspiele gefestigt und durch einfache, aber effektive Selbstverteidigungstechniken ergänzt.</p>
      <p>Wir zeigen ihnen in unserem Kurs „Sichere Kinder – Sicherer Start“ Mittel und Möglichkeiten, wie sie Belastungssituationen sicher und souverän bewältigen können. Speziell konzipierte Rangel- und Raufspiele unterstützen eine praxisnahe Umsetzung der Inhalte und garantieren jede Menge Spaß und einen intensiven Erfahrungsraum für alle teilnehmenden Kinder.</p>
    </div>

    <div class="col col--l2">
      <p>Der Kurs beinhaltet 4 Einheiten mit je 45 Minuten:</p>
      <ol class="units">
        <li><strong>1. Einheit</strong>Wie gehe ich selbstsicher mit neuen Mitschülern um und wie finde ich neue Freunde?</li>
        <li><strong>2. Einheit</strong>Wie verhalte ich mich souverän in Streitsituationen?</li>
        <li><strong>3. Einheit</strong>Wie verhalte ich mich auf dem Schulweg und wie komme ich sicher nach Hause?</li>
        <li><strong>4. Einheit</strong>Wie gehe ich mit Erfolgserlebnissen um und wie reagiere ich auf Rückschläge?</li>
      </ol>
    </div>

    <div class="photo photo--kids" role="img" aria-label="Foto: Schulkinder mit Rucksäcken laufen von hinten gesehen einen Schulflur entlang"></div>

    <div class="brand-name">BODENLERNWERK</div>
    <div class="page-number">SEITE 8</div>
  </section>

  <section class="page page--right">
    <div class="photo photo--mats" role="img" aria-label="Foto: gerollte rote Gymnastikmatten und graue Blöcke auf hellem Hallenboden"></div>
    <h2 class="headline">Kursangebot</h2>
    <div class="headline-rule"></div>

    <div class="col col--r1">
      <p><strong>Toben – Tollen – Balancieren</strong><br>Speziell für Kindergärten, Schulen und sonstige Pädagogische Einrichtungen (Kinder- und Jugendheim etc.).</p>
      <p>Gruppengröße und zeitlicher Rahmen wird in Absprache mit dem pädagogischen Personal vor Ort bestimmt. Schwerpunkte können in den Bereichen</p>
    </div>
    <div class="col col--r2">
      <p>der Mobbing- und Gewaltprävention, im Antiaggressionstraining und der Jungen-/Männerarbeit gesetzt werden.</p>
      <p><strong>Sichere Kinder – sicherer Start</strong><br>Speziell für Kindergärten (4 x 45 min., max. 20 Teilnehmer) und Grundschulen bis einschließlich 5. Klasse (4 x 45 min, 20 – 30 Teilnehmer).</p>
    </div>

    <aside class="quote-box quote-box--a">
      <div class="quote-label">Lehrerstimme</div>
      <div class="quote-author">
        <svg width="10" height="7" viewBox="0 0 10 7" aria-hidden="true"><path d="M5 0 10 2.3 5 4.6 0 2.3Z M2 3.6V5.6C3.5 7 6.5 7 8 5.6V3.6L5 5Z" fill="#fff"/></svg>
        <span>Jonas Albrecht<br>(Realschule Lindenau)</span>
      </div>
      <p class="quote-text quote-text--italic">„Es war auch für mich sehr eindrucksvoll, meine Jungs mal aus einer andern Position zu betrachten. Ihr habt den Unterricht sehr systematisch aufgebaut und gut organisiert. Die Jungs haben mit großem Interesse zugehört und waren an euren Lippen gehangen. Unheimlich motivierend habt ihr Theorie und Praxis gemischt.“</p>
    </aside>

    <aside class="quote-box quote-box--b">
      <div class="quote-label">Lehrerstimme</div>
      <div class="quote-author">
        <svg width="10" height="7" viewBox="0 0 10 7" aria-hidden="true"><path d="M5 0 10 2.3 5 4.6 0 2.3Z M2 3.6V5.6C3.5 7 6.5 7 8 5.6V3.6L5 5Z" fill="#fff"/></svg>
        <span>Carla Neumeier<br>(Grundschule Hohenfeld)</span>
      </div>
      <p class="quote-text">„Timo &amp; Tobi verstanden es hervorragend, mit sportlichem Können und pädagogischem Geschick die Aufmerksamkeit unserer quirligen Zweitklässler auf sich zu bannen, um ihnen zunächst in verschiedenen Gruppen- und Partnerübungen die Wichtigkeit gegenseitiger Rücksichtnahme zu vermitteln... Begeisterte Kinder, die sich teilweise von einer ganz neuen Seite gezeigt haben.“</p>
    </aside>

    <div class="brand-name">BODENLERNWERK</div>
    <div class="page-number">SEITE 9</div>
  </section>
</main>
</body>
</html>
```